Whitmore Business Card Design

The name of the business is Dara Whitmore, CPA LLC
The service that we offer is Accounting, Tax & Consulting Services. I need it to have the following items:
Dara Whitmore, Principal
Phone Number
Email Address
Physical Address

I have attached the company logo, one in black and one in white. Please provide a design in black background and the other in white background. Please include "Accounting, Tax & Consulting Services". I want the business card to be clean and very professional.

```html
<!DOCTYPE html>
<html lang="en">
<head>
<meta charset="utf-8">
<title>Dara Whitmore, CPA LLC — Business Card</title>
<link href="https://fonts.googleapis.com/css2?family=Montserrat:wght@400;500;600;700&display=swap" rel="stylesheet">
<style>
  :root {
    --canvas: #ffffff;
    --ink: #000000;
    --paper: #ffffff;
    --charcoal: #3a3a3a;
    --grey: #8c8c8c;
    --crimson: #991b1f;
    --edge: #a8a8a8;
  }
  * { margin: 0; padding: 0; box-sizing: border-box; }
  html, body { width: 1200px; height: 1000px; overflow: hidden; background: var(--canvas); }
  body { position: relative; font-family: "Montserrat", sans-serif; }

  .card { position: absolute; left: 204px; width: 792px; height: 453px; overflow: hidden; }
  .card--front { top: 29px; background: var(--ink); color: var(--paper); }
  .card--back { top: 518px; background: var(--paper); border: 1px solid var(--edge); }

  .brand { position: absolute; display: flex; align-items: center; }
  .brand__mark { flex: none; }
  .brand__text { display: flex; flex-direction: column; }
  .brand__name { font-weight: 600; text-transform: uppercase; letter-spacing: 0.02em; white-space: nowrap; line-height: 1; }
  .brand__title { font-weight: 600; text-transform: uppercase; letter-spacing: 0.08em; white-space: nowrap; line-height: 1; }

  .card--front .brand { left: 130px; top: 162px; }
  .card--front .brand__mark { width: 66px; height: 66px; background: var(--paper); margin-right: 24px; }
  .card--front .brand__name { font-size: 29px; color: var(--paper); }
  .card--front .brand__title { font-size: 19px; color: var(--paper); margin-top: 9px; }

  .tagline { position: absolute; left: 0; right: 0; top: 354px; text-align: center; font-size: 18px; font-weight: 400; letter-spacing: 0.01em; }

  .card--back .brand { left: 197px; top: 80px; }
  .card--back .brand__mark { width: 48px; height: 48px; background: var(--crimson); margin-right: 19px; }
  .card--back .brand__name { font-size: 22px; color: var(--charcoal); }
  .card--back .brand__title { font-size: 15px; color: var(--grey); margin-top: 6px; }

  .contact-band { position: absolute; left: 0; right: 0; top: 188px; height: 170px; background: var(--crimson); color: var(--paper); }
  .person { position: absolute; left: 116px; top: 54px; }
  .person__name { font-size: 24px; font-weight: 700; }
  .person__role { font-size: 18px; font-weight: 400; margin-top: 14px; }
  .contact-band__divider { position: absolute; left: 345px; top: 28px; width: 1px; height: 113px; background: rgba(255,255,255,0.7); }
  .contact-list { position: absolute; left: 389px; top: 25px; list-style: none; }
  .contact-list__item { display: flex; align-items: center; height: 28px; font-size: 18px; margin-bottom: 16.5px; }
  .contact-list__icon { width: 28px; height: 28px; margin-right: 21px; flex: none; }
</style>
</head>
<body>
  <section class="card card--front" aria-label="Card front">
    <div class="brand">
      <span class="brand__mark" aria-hidden="true"></span>
      <div class="brand__text">
        <span class="brand__name">Dara Whitmore, CPA, LLC</span>
        <span class="brand__title">Certified Public Accountant</span>
      </div>
    </div>
    <p class="tagline">Accounting, Tax &amp; Consulting Services</p>
  </section>

  <section class="card card--back" aria-label="Card back">
    <div class="brand">
      <span class="brand__mark" aria-hidden="true"></span>
      <div class="brand__text">
        <span class="brand__name">Dara Whitmore, CPA, LLC</span>
        <span class="brand__title">Certified Public Accountant</span>
      </div>
    </div>

    <div class="contact-band">
      <div class="person">
        <p class="person__name">Dara Whitmore</p>
        <p class="person__role">Principal</p>
      </div>
      <span class="contact-band__divider"></span>
      <ul class="contact-list">
        <li class="contact-list__item">
          <svg class="contact-list__icon" viewBox="0 0 28 28" aria-hidden="true">
            <circle cx="14" cy="14" r="14" fill="#ffffff"/>
            <path d="M9.6 7.5c.5-.4 1.2-.3 1.5.2l1.5 2.3c.3.5.2 1.1-.2 1.4l-1 .8c.7 1.6 2 2.9 3.6 3.7l.8-1c.3-.4 1-.5 1.4-.2l2.3 1.5c.5.3.6 1 .2 1.5l-1 1.2c-.5.6-1.3.8-2 .6-4-1.3-7.1-4.4-8.4-8.4-.2-.7 0-1.5.6-2z" fill="#991b1f"/>
          </svg>
          <span>+0123456789</span>
        </li>
        <li class="contact-list__item">
          <svg class="contact-list__icon" viewBox="0 0 28 28" aria-hidden="true">
            <circle cx="14" cy="14" r="14" fill="#ffffff"/>
            <rect x="7.5" y="9.5" width="13" height="9" rx="1" fill="none" stroke="#991b1f" stroke-width="1.5"/>
            <path d="M8 10l6 5 6-5" fill="none" stroke="#991b1f" stroke-width="1.5"/>
          </svg>
          <span>darawhitmore@ledgerpost.com</span>
        </li>
        <li class="contact-list__item">
          <svg class="contact-list__icon" viewBox="0 0 28 28" aria-hidden="true">
            <circle cx="14" cy="14" r="14" fill="#ffffff"/>
            <path d="M14 6.5c-3 0-5.2 2.3-5.2 5.1 0 3.6 5.2 9.4 5.2 9.4s5.2-5.8 5.2-9.4c0-2.8-2.2-5.1-5.2-5.1z" fill="#991b1f"/>
            <circle cx="14" cy="11.6" r="1.9" fill="#ffffff"/>
          </svg>
          <span>123 Street, Lorem Ipsum</span>
        </li>
      </ul>
    </div>
  </section>
</body>
</html>
```